Ovaro Letterhead

Need a fresh looking design. We are a IT service company and I would like some elements of the logo to flow through. I have included the logo as an attachment. I have also included business card design as it might help with the design.

Industry/Entity Type

Business

```html
<!DOCTYPE html>
<html lang="en">
<head>
<meta charset="utf-8">
<title>Ovaro Letterhead</title>
<link href="https://fonts.googleapis.com/css2?family=Open+Sans:wght@400;600&family=Mr+Dafoe&display=swap" rel="stylesheet">
<style>
  :root {
    --bg: #f1f1f1;
    --paper: #ffffff;
    --folder: #2f2f2f;
    --folder-edge: #3a3a3a;
    --ink: #3d3d3d;
    --muted: #7a7a7a;
    --green: #8dc63f;
    --grey: #8c959c;
    --band: #333333;
  }
  * { box-sizing: border-box; margin: 0; padding: 0; }
  html, body { width: 1200px; height: 1000px; overflow: hidden; }
  body {
    background: var(--bg);
    font-family: "Open Sans", Arial, sans-serif;
    color: var(--ink);
    position: relative;
  }
  .folder-cover {
    position: absolute;
    left: 90px; top: 190px;
    width: 440px; height: 622px;
    background: linear-gradient(160deg, var(--folder-edge), var(--folder));
    box-shadow: 0 6px 18px rgba(0,0,0,.18);
  }
  .brand {
    display: flex; align-items: center; gap: 6px;
    font-weight: 600; color: var(--green);
  }
  .brand-square { width: 10px; height: 10px; background: var(--green); }
  .folder-cover .brand { position: absolute; top: 34px; right: 34px; font-size: 30px; }
  .folder-cover .brand-square { width: 14px; height: 14px; }

  .letterhead {
    position: absolute;
    left: 670px; top: 190px;
    width: 440px; height: 622px;
    background: var(--paper);
    box-shadow: 0 6px 18px rgba(0,0,0,.14);
  }
  .letterhead .brand { position: absolute; top: 30px; left: 34px; font-size: 24px; }
  .contact-block {
    position: absolute; top: 96px; right: 30px; width: 96px;
    font-size: 6px; line-height: 1.6; color: var(--muted);
    font-style: normal;
  }
  .contact-block .contact-name { color: var(--green); font-weight: 600; }
  .salutation { position: absolute; top: 132px; left: 34px; font-size: 9px; }
  .letter-body {
    position: absolute; top: 162px; left: 50px; width: 330px;
    font-size: 7.5px; line-height: 1.5;
  }
  .letter-body p + p { margin-top: 10px; }
  .signature {
    position: absolute; top: 366px; left: 230px;
    font-family: "Mr Dafoe", cursive; font-size: 26px; color: #222;
  }
  .footer-band { position: absolute; left: 0; bottom: 0; width: 440px; height: 20px; display: block; }
</style>
</head>
<body>
  <section class="folder-cover">
    <div class="brand"><span class="brand-name">Ovaro</span><span class="brand-square"></span></div>
  </section>

  <section class="letterhead">
    <div class="brand"><span class="brand-name">Ovaro</span><span class="brand-square"></span></div>

    <address class="contact-block">
      <div class="contact-name">Ovaro</div>
      <div>PO Box 118, Kelmore 2041</div>
      <div>T +02 5550 1427</div>
      <div>F +02 5550 1428</div>
      <div>hello@ovaro.example</div>
      <div>www.ovaro.example</div>
    </address>

    <div class="salutation">Dear Client,</div>

    <div class="letter-body">
      <p>Lorem ipsum dolor sit amet, consectetur adipiscing elit. Nulla sodales nisi vitae Lorem ipsum dolor sit amet, consectetur adipiscing elit. Suspendisse feugiat eros nisl, a facilisis risus eleifend sed. Aliquam mauris enim, fermentum eu lacinia sit amet, laoreet eu leo. Nullam eleifend nulla in libero tristique, ac vulputate odio tincidunt. Etiam non condimentum tortor. Integer suscipit neque nec odio porttitor cursus. Phasellus a sapien blandit, suscipit justo id, condimentum risus. Pellentesque urna est, interdum id mattis dui molestie ut. Nullam volutpat ut quam commodo faucibus. Pellentesque justo risus, id placerat dum in elit quis, pharetra elementum orci. Nam pharetra velit molestie justo scelerisque.</p>
      <p>Ut vitae interdum diam, in euismod ante. Pellentesque volutpat, risus sit amet sodales hendrerit, mi turpis vulputate dolor, eget cursus nulla eros nec tellus. Nulla tincidunt molestie libero vel pretium. Donec condimentum nulla sit amet risus semper imperdiet. Duis congue eros nec diam blandit, et pellentesque sapien auctor. Curabitur iaculis enim lectus, in imperdiet mauris mattis eget. Etiam ac ornare metus. Mauris risus leo, egestas at dolor a, ultrices adipiscing est. Nunc faucibus scelerisque mollis. Pellentesque aliquet mauris tellus, id dignissim risus viverra et. Mauris venenatis lobortis eros. Nam id diam in ligula malesuada feugiat. Cras turpis felis, aliquet id mauris elementum, feugiat ultricies nisl.</p>
    </div>

    <div class="signature">Alex Marlow</div>

    <svg class="footer-band" viewBox="0 0 440 20" aria-hidden="true">
      <polygon points="0,0 312,0 300,20 0,20" fill="var(--band)"/>
      <polygon points="312,0 392,0 380,20 300,20" fill="var(--green)"/>
      <polygon points="392,0 440,0 440,20 380,20" fill="var(--grey)"/>
    </svg>
  </section>
</body>
</html>
```